Holbys Pet Care

Hi. I need a business card /logo for my pet care business. Im thinking about a dogs paw print. Although i do look after other pets so don't want to restrict my self. Open to suggestions on colour etc but like greens and purples.The name of my business is holby's pet care. The logo could be just an image or have holbys power care on it. An option to do either would be great. For the winner i also would like a Web page (word press template if possible) designed if you can, of course I'll pay additional for this. Look forward to your ideas!

```html
<!DOCTYPE html>
<html lang="en">
<head>
<meta charset="utf-8">
<title>Holbys Pet Care – Business Card</title>
<link rel="stylesheet" href="https://fonts.googleapis.com/css2?family=Arimo:wght@400;700&family=Sniglet:wght@800&display=swap">
<style>
  :root {
    --purple: #8e2a8c;
    --green: #8cc63f;
    --white: #ffffff;
    --ink: #1a1a1a;
    --backdrop: #d6d6d6;
    --text-font: "Arimo", Arial, sans-serif;
    --display-font: "Sniglet", "Arial Rounded MT Bold", sans-serif;
  }
  * { box-sizing: border-box; margin: 0; padding: 0; }
  html, body {
    width: 1200px; height: 902px; overflow: hidden;
    background: var(--backdrop);
  }
  .stage { position: relative; width: 1200px; height: 902px; }

  .card {
    position: absolute; left: 250px; width: 700px; height: 400px;
    background: var(--purple); overflow: hidden;
    box-shadow: 0 6px 16px rgba(0,0,0,0.25);
    font-family: var(--text-font);
  }
  .card--back { top: 35px; }
  .card--front { top: 467px; }

  .band-white { position: absolute; left: 0; right: 0; background: var(--white); }
  .card--back .band-white { top: 125px; height: 150px; }
  .card--front .band-white { top: 100px; height: 145px; }

  .brand { position: absolute; display: flex; align-items: center; gap: 14px; }
  .brand__dot { border-radius: 50%; background: var(--green); flex: none; }
  .brand__name { font-family: var(--text-font); font-weight: 700; line-height: 1; }
  .brand__tagline { font-size: 12px; font-weight: 700; margin-top: 5px; }

  .card--back .brand { left: 150px; top: 160px; }
  .card--back .brand__dot { width: 62px; height: 62px; }
  .card--back .brand__name { font-size: 44px; color: var(--purple); }
  .card--back .brand__tagline { color: var(--ink); font-size: 13px; }

  .card--front .brand { left: 130px; top: 24px; }
  .card--front .brand__dot { width: 46px; height: 46px; }
  .card--front .brand__name { font-size: 30px; color: var(--white); }
  .card--front .brand__tagline { color: var(--white); font-size: 10.5px; }

  .owner-name {
    position: absolute; left: 60px; top: 118px;
    font-family: var(--display-font); font-weight: 800;
    font-size: 84px; color: var(--purple); line-height: 1;
  }
  .pet-silhouettes {
    position: absolute; left: 450px; top: 120px;
    width: 215px; height: 115px;
    background: var(--green); border-radius: 8px;
  }

  .contact {
    position: absolute; left: 50px; top: 275px;
    color: var(--white); font-size: 17px; line-height: 1.6;
  }
  .contact__value { color: var(--green); }
  .contact__sep { margin: 0 10px; }
</style>
</head>
<body>
<main class="stage">

  <section class="card card--back" aria-label="Card back">
    <div class="band-white"></div>
    <div class="brand">
      <span class="brand__dot"></span>
      <div>
        <div class="brand__name">Holbys Pet Care</div>
        <div class="brand__tagline">Dog walking.&nbsp; Pet boarding.&nbsp; Home visits for feeding etc.</div>
      </div>
    </div>
  </section>

  <section class="card card--front" aria-label="Card front">
    <div class="band-white"></div>
    <div class="brand">
      <span class="brand__dot"></span>
      <div>
        <div class="brand__name">Holbys Pet Care</div>
        <div class="brand__tagline">Dog walking.&nbsp; Pet boarding.&nbsp; Home visits for feeding etc.</div>
      </div>
    </div>
    <div class="owner-name">“Holby”</div>
    <div class="pet-silhouettes" role="img" aria-label="Green silhouettes of a dog, a cat and a rabbit"></div>
    <div class="contact">
      <p>Tel. no.: <span class="contact__value">000-000-000</span><span class="contact__sep">•</span>E-mail: <span class="contact__value">holby@holbyspetcare.co.uk</span></p>
      <p>FB: <span class="contact__value">holbyspetcare@facebook.com</span></p>
    </div>
  </section>

</main>
</body>
</html>
```